New Zealand Luggage Importer Needs Business Cards

We need professional, creative and fashionable business cards created.
We are based in New Zealand and import and distribute high-end, quality, fashionable and durable luggage.
We pride ourselves on selling the very best quality luggage, second only to 1 brand (which we won't mention here)...we use the same manufacturer. However, our prices are much more reasonable.
Industry/Entity Type
Business
Contact Information for Business Card
Mark Dunsley
027 512 4068
3/17 Harlow Street, Pinecrest Flats, Auckland, 0614
PO Box 204377, Fernside, Auckland 0731
09-528-3916
sales@brivancases.co.nz / www.brivancases.co.nz

```html
<!DOCTYPE html>
<html lang="en">
<head>
<meta charset="utf-8">
<title>Brivan Cases – Business Card</title>
<link href="https://fonts.googleapis.com/css2?family=Roboto:wght@400;700&family=Roboto+Condensed:wght@700&display=swap" rel="stylesheet">
<style>
  :root {
    --backdrop: #d9d4cd;
    --card-top: #f4f1ec;
    --card-bottom: #ebe6df;
    --card-edge: #cfc8bf;
    --ink: #1c1c1c;
    --ink-soft: #3a3a3a;
    --gold: #8a6a3c;
    --gold-light: #b08c55;
  }
  * { margin: 0; padding: 0; box-sizing: border-box; }
  html, body {
    width: 1200px;
    height: 970px;
    overflow: hidden;
    background: var(--backdrop);
    font-family: "Roboto", Arial, sans-serif;
    color: var(--ink);
  }
  .card {
    position: absolute;
    left: 360px;
    top: 54px;
    width: 480px;
    height: 862px;
    background: linear-gradient(180deg, var(--card-top), var(--card-bottom));
    border: 1px solid var(--card-edge);
    box-shadow: 0 18px 40px rgba(60, 48, 34, 0.18);
  }
  .brand-name {
    position: absolute;
    left: 46px;
    top: 86px;
    font-weight: 700;
    font-size: 36px;
    letter-spacing: 1px;
    color: var(--ink);
    white-space: nowrap;
  }
  .name-tab {
    position: absolute;
    left: 0;
    top: 368px;
    width: 14px;
    height: 52px;
    background: linear-gradient(180deg, var(--gold-light), var(--gold));
    border-radius: 0 6px 6px 0;
  }
  .person-name {
    position: absolute;
    left: 46px;
    top: 352px;
    font-family: "Roboto Condensed", "Arial Narrow", sans-serif;
    font-weight: 700;
    font-size: 40px;
    color: var(--gold);
  }
  .person-role {
    position: absolute;
    left: 47px;
    top: 408px;
    font-size: 18px;
    color: var(--ink-soft);
  }
  .contact-list {
    position: absolute;
    left: 46px;
    top: 474px;
    list-style: none;
  }
  .contact-list li {
    display: flex;
    align-items: center;
    height: 37px;
    font-size: 22px;
    color: var(--ink);
  }
  .contact-icon {
    width: 18px;
    height: 18px;
    margin-right: 13px;
    flex: none;
    fill: var(--gold);
  }
  .address-block {
    position: absolute;
    left: 46px;
    top: 664px;
    font-size: 22px;
    line-height: 28px;
    color: var(--ink);
  }
  .address-block p + p { margin-top: 8px; }
</style>
</head>
<body>
  <div class="card">
    <div class="brand-name">BRIVAN CASES</div>

    <div class="name-tab"></div>
    <div class="person-name">Mark Dunsley</div>
    <div class="person-role">Owner</div>

    <ul class="contact-list">
      <li>
        <svg class="contact-icon" viewBox="0 0 24 24" aria-hidden="true"><path d="M6.6 10.8c1.4 2.8 3.8 5.1 6.6 6.6l2.2-2.2c.3-.3.7-.4 1-.2 1.1.4 2.3.6 3.6.6.6 0 1 .4 1 1V20c0 .6-.4 1-1 1C10.6 21 3 13.4 3 4c0-.6.4-1 1-1h3.5c.6 0 1 .4 1 1 0 1.3.2 2.5.6 3.6.1.3 0 .7-.2 1z"/></svg>
        027 512 4068
      </li>
      <li>
        <svg class="contact-icon" viewBox="0 0 24 24" aria-hidden="true"><path d="M7 1h10c1.1 0 2 .9 2 2v18c0 1.1-.9 2-2 2H7c-1.1 0-2-.9-2-2V3c0-1.1.9-2 2-2zm0 3v14h10V4H7zm5 15.2a1.2 1.2 0 100 2.4 1.2 1.2 0 000-2.4z"/></svg>
        09-528-3916
      </li>
      <li>
        <svg class="contact-icon" viewBox="0 0 24 24" aria-hidden="true"><path d="M2 5h20v14H2V5zm2 2v.4l8 5.2 8-5.2V7H4zm0 2.8V17h16V9.8l-8 5.2-8-5.2z"/></svg>
        sales@brivancases.co.nz
      </li>
      <li>
        <svg class="contact-icon" viewBox="0 0 24 24" aria-hidden="true"><path d="M12 2a10 10 0 100 20 10 10 0 000-20zm6.9 6h-3a15 15 0 00-1.3-3.9A8 8 0 0118.9 8zM12 4c.8 1.2 1.5 2.5 1.9 4h-3.8c.4-1.5 1.1-2.8 1.9-4zM4.3 14a8 8 0 010-4h3.4a16 16 0 000 4H4.3zm.8 2h3a15 15 0 001.3 3.9A8 8 0 015.1 16zm3-8h-3a8 8 0 014.3-3.9C8.8 5.3 8.4 6.6 8.1 8zM12 20c-.8-1.2-1.5-2.5-1.9-4h3.8c-.4 1.5-1.1 2.8-1.9 4zm2.3-6H9.7a14 14 0 010-4h4.6a14 14 0 010 4zm.3 5.9c.6-1.2 1-2.5 1.3-3.9h3a8 8 0 01-4.3 3.9zm1.7-5.9a16 16 0 000-4h3.4a8 8 0 010 4h-3.4z"/></svg>
        www.brivancases.co.nz
      </li>
    </ul>

    <div class="address-block">
      <p>3/17 Harlow Street, Pinecrest Flats<br>Auckland, 0614</p>
      <p>PO Box 204377, Fernside<br>Auckland 0731</p>
    </div>
  </div>
</body>
</html>
```